Banner Ads for Online Poker Promotion

We are an online poker network, the QRX (www.theqrx.eu). We are looking for a small selection of web banner ads for our latest promotion.

Banner sizes that we need are:
- 196x523 (static .psd and .png)
- 199x129 (static .psd and .png)
- 447x426 (static .psd and .png)
- 500x400 (static .psd and .png)
- 697x167 (static .psd and .png)
- 460x60 (animated .gif)

The promotion name is ‘Spin & Win Haul’ (or ‘SNW Haul’) and the concept is that certain Sit & Go tournaments have money added to the prize pool. Basically, free cash for Sit & Go players.

(If you don’t know poker, a ‘Sit & Go’ is a tournament which starts when a specific number of players join, as opposed to a scheduled tournament which starts at a specific time).

The promotion starts on November 3rd.

Guidelines:

The name of the promotion, ‘Spin & Win Haul’ or ‘SNW Haul’, should feature prominently in the banners.

The strap line can be ‘Get Your Share of the Loot’, ‘Added Money in SNGs’ or something similar (feel free to be creative).

Our network logo (attached) must feature on the animated .gif. It is optional on the other banners.

Examples of past promotional imagery can be found on our website, in particular these pages: http://www.theqrx.eu/promotions/ and http://www.theqrx.eu/promotions/archived-promotions/ . Our last promotion was crowdsourced and the details of that and the winner can be found here: http://gigs.artfolder.com/gig.aspx?id=431257

We are looking to go in a more modern and risqué direction than the past, in order to stand out from competition which is very bland.

Common poker imagery –cards, chips, suit icons etc – or objects associated with live poker (tables, etc) is a little clichéd. It can be included if it has a clear purpose. But don’t just put flying cards or suit symbols in there for no reason.

More like Zephyr 4/5, less like Zephyr 3

Think flat, modern, glamour, clean, fresh, bright, rock music, extreme sports, and the Iron Vale!

Most of our customers are 18-35, male, and we have a strong European focus.

As we are a gaming company, the banners must not encourage underage play, problem gambling, or associate gambling with sexual or social success.

If any further guidance is needed please don’t hesitate to ask!

```html
<!DOCTYPE html>
<html lang="en">
<head>
<meta charset="utf-8">
<title>Spin &amp; Win Haul – Banner Set</title>
<link href="https://fonts.googleapis.com/css2?family=Alfa+Slab+One&family=Montserrat:wght@400&display=swap" rel="stylesheet">
<style>
  :root{
    --page:#000;
    --navy-deep:#04121c;
    --navy:#0b2c40;
    --teal:#1d5f7c;
    --yellow:#ffd22e;
    --orange:#ffa20a;
    --orange-light:#ffd23a;
    --plate:#1a1c1f;
    --plate-edge:#e4e6e8;
    --silver:#f2f2f2;
    --silver-dark:#9a9ea3;
    --ribbon-text:#3a2a00;
    --logo:#dfe8ee;
  }
  *{box-sizing:border-box;margin:0;padding:0}
  html,body{width:1097px;height:1200px;overflow:hidden;background:var(--page)}
  .sheet{position:absolute;left:0;top:0;width:1045px;height:1143px;transform:scale(1.05);transform-origin:0 0}
  .banner{
    position:absolute;overflow:hidden;border:1px solid #1e3a4c;
    background:
      radial-gradient(ellipse 60% 55% at 50% 0%, rgba(180,220,235,.55), rgba(60,130,160,.25) 55%, transparent 80%),
      radial-gradient(ellipse at 50% 40%, var(--teal), var(--navy) 60%, var(--navy-deep));
    font-family:"Alfa Slab One", serif;
  }
  .ribbon{
    position:absolute;left:0;top:0;background:var(--yellow);
    clip-path:polygon(0 0,100% 0,0 100%);
  }
  .ribbon-text{
    position:absolute;left:0;top:0;color:var(--ribbon-text);text-align:center;
    line-height:1.05;transform-origin:center;white-space:nowrap;
  }
  .network-name{
    position:absolute;color:var(--logo);font-family:"Montserrat", sans-serif;font-weight:400;
    letter-spacing:.04em;text-align:center;line-height:1;
  }
  .plaque{
    position:absolute;background:var(--plate);border-radius:12px;
    border:solid var(--plate-edge);
    box-shadow:0 6px 14px rgba(0,0,0,.6), inset 0 0 0 2px #000;
    display:flex;flex-direction:column;align-items:center;justify-content:center;
    transform:rotate(-8deg);line-height:.98;text-align:center;
  }
  .title-top{
    background:linear-gradient(180deg,var(--orange-light) 0%,var(--orange-light) 45%,var(--orange) 55%,var(--orange) 100%);
    -webkit-background-clip:text;background-clip:text;color:transparent;white-space:nowrap;
  }
  .title-bottom{
    background:linear-gradient(180deg,var(--silver) 0%,var(--silver) 50%,var(--silver-dark) 52%,#d8dadc 100%);
    -webkit-background-clip:text;background-clip:text;color:transparent;white-space:nowrap;
  }
  .tagline{
    position:absolute;color:var(--yellow);transform:rotate(-8deg);line-height:1.05;
    text-shadow:0 2px 4px rgba(0,0,0,.6);white-space:nowrap;
  }
  .tall-band{
    position:absolute;left:0;top:0;width:100%;height:48px;background:var(--yellow);
    color:var(--ribbon-text);text-align:center;font-size:13px;line-height:1.05;padding-top:10px;
  }
</style>
</head>
<body>
<div class="sheet">

  <!-- Leaderboard 697x167 -->
  <section class="banner" style="left:49px;top:49px;width:699px;height:169px">
    <div class="ribbon" style="width:112px;height:108px"></div>
    <div class="ribbon-text" style="left:-2px;top:28px;width:90px;font-size:12px;transform:rotate(-44deg)">STARTS<br>NOVEMBER 3</div>
    <div class="network-name" style="left:28px;top:126px;width:90px;font-size:24px">QRX</div>
    <div class="plaque" style="left:170px;top:26px;width:236px;height:114px;border-width:5px">
      <div class="title-top" style="font-size:28px">SPIN &amp; WIN</div>
      <div class="title-bottom" style="font-size:40px">HAUL</div>
    </div>
    <div class="tagline" style="left:446px;top:36px;font-size:24px">GET YOUR<br>SHARE OF THE<br>LOOT!</div>
  </section>

  <!-- Skyscraper 196x523 -->
  <section class="banner" style="left:798px;top:49px;width:198px;height:525px">
    <div class="tall-band">STARTS<br>NOVEMBER 3</div>
    <div class="network-name" style="left:0;top:122px;width:100%;font-size:28px">QRX</div>
    <div class="plaque" style="left:16px;top:196px;width:166px;height:160px;border-width:5px">
      <div class="title-top" style="font-size:30px;line-height:1">SPIN &amp;<br>WIN</div>
      <div class="title-bottom" style="font-size:36px">HAUL</div>
    </div>
    <div class="tagline" style="left:26px;top:398px;font-size:20px;text-align:left">GET YOUR<br>&nbsp;&nbsp;&nbsp;SHARE OF<br>THE LOOT!</div>
  </section>

  <!-- Medium rectangle 500x400 -->
  <section class="banner" style="left:49px;top:241px;width:502px;height:401px">
    <div class="ribbon" style="width:136px;height:132px"></div>
    <div class="ribbon-text" style="left:0;top:34px;width:104px;font-size:13px;transform:rotate(-44deg)">STARTS<br>NOVEMBER 3</div>
    <div class="network-name" style="left:0;top:56px;width:100%;font-size:30px">QRX</div>
    <div class="plaque" style="left:44px;top:96px;width:410px;height:180px;border-width:7px;border-radius:16px">
      <div class="title-top" style="font-size:50px">SPIN &amp; WIN</div>
      <div class="title-bottom" style="font-size:76px">HAUL</div>
    </div>
    <div class="tagline" style="left:64px;top:314px;font-size:26px">GET YOUR SHARE<br>&nbsp;&nbsp;&nbsp;&nbsp;&nbsp;&nbsp;&nbsp;&nbsp;OF THE LOOT</div>
  </section>

  <!-- Small 199x129 -->
  <section class="banner" style="left:574px;top:241px;width:201px;height:131px">
    <div class="plaque" style="left:26px;top:14px;width:150px;height:72px;border-width:3px;border-radius:7px">
      <div class="title-top" style="font-size:17px">SPIN &amp; WIN</div>
      <div class="title-bottom" style="font-size:25px">HAUL</div>
    </div>
    <div class="tagline" style="left:42px;top:96px;font-size:10px">GET YOUR SHARE<br>&nbsp;&nbsp;&nbsp;&nbsp;&nbsp;OF THE LOOT</div>
  </section>

  <!-- Square 447x426 -->
  <section class="banner" style="left:49px;top:666px;width:449px;height:428px">
    <div class="ribbon" style="width:136px;height:132px"></div>
    <div class="ribbon-text" style="left:0;top:34px;width:104px;font-size:13px;transform:rotate(-44deg)">STARTS<br>NOVEMBER 3</div>
    <div class="network-name" style="left:0;top:64px;width:100%;font-size:30px">QRX</div>
    <div class="plaque" style="left:26px;top:106px;width:394px;height:176px;border-width:7px;border-radius:16px">
      <div class="title-top" style="font-size:48px">SPIN &amp; WIN</div>
      <div class="title-bottom" style="font-size:74px">HAUL</div>
    </div>
    <div class="tagline" style="left:46px;top:320px;font-size:26px">GET YOUR SHARE<br>&nbsp;&nbsp;&nbsp;&nbsp;&nbsp;&nbsp;&nbsp;&nbsp;OF THE LOOT</div>
  </section>

</div>
</body>
</html>
```